依頼詳細
海外のセルフサービス式飲食店で使用します。各商品の前につける値札の作成をお願します。

Karaage Chicken $2.8
炸鸡
가라아게 치킨
鶏の唐揚げ
Pollo frito

こちらの商品の値札のデザイン作成していただき、採用決定後に、デザインはそのままその他約60品の商品名や金額の入力をお願いさせて頂きたいと思っています。

英語をメインに
日本語、中国語、韓国語、スペイン語
も併記したく思っています。

英語圏(オーストラリア)にある日本食レストランですので英語の次に日本語が大きくなって、他3ヶ国語が小さくても構いません。

サイズは" 3.5cm x 6cm "
でお願いいたします。

納品の際には、イラストレーターまたはフォトショップで文字の編集が可能なデータをお願いします。

ロゴを添付しています。
ロゴは有り、無し、または ロゴ内のキャラクター部分のみの使用でも構いません。ロゴの色や印象に合うデザインを希望しています。

よろしくお願いいたします。
記載項目

商品名:Karaage Chicken
価格:$2.8
日本語:鶏の唐揚げ
中国語:炸鸡
韓国語:가라아게 치킨
スペイン語:Pollo frito

ベジタリアンの商品にはベジタリアン商品と伝わるようなマーク
サイズ
3.5cm x 6cm
ページ数
片面
希望イメージ
シンプル 複雑
単色 カラフル
暗い 明るい
日常 高級
遊び心 厳粛
未来的 伝統的
女性的 男性的
希望する色
黄・オレンジ系

シンプルで見やすいのでこちらを選ばせて頂きました!

この度はご応募いただきありがとうございます。素敵なデザインを数々ご提案いただきましたが一つに絞らせていただきました。

また今後機会がありましたらよろしくお願いいたします

```html
<!DOCTYPE html>
<html lang="en">
<head>
<meta charset="UTF-8">
<title>Price Tag – Karaage Chicken</title>
<link href="https://fonts.googleapis.com/css2?family=Quicksand:wght@500;700&family=Noto+Sans+JP:wght@500&family=Noto+Sans+KR:wght@500&family=Noto+Sans+SC:wght@500&display=swap" rel="stylesheet">
<style>
  :root {
    --tag-red: #ef4a3f;
    --tag-white: #ffffff;
  }
  html, body {
    margin: 0;
    padding: 0;
    width: 700px;
    height: 1200px;
    overflow: hidden;
    background: var(--tag-red);
  }
  .price-tag {
    position: relative;
    width: 700px;
    height: 1200px;
    background: var(--tag-red);
    color: var(--tag-white);
    font-family: "Quicksand", sans-serif;
    font-weight: 500;
  }
  .brand {
    position: absolute;
    top: 92px;
    right: 76px;
    display: flex;
    align-items: center;
    gap: 14px;
  }
  .brand-name {
    font-size: 22px;
    font-weight: 500;
    color: var(--tag-white);
    letter-spacing: 0.5px;
  }
  .brand-badge {
    width: 104px;
    height: 104px;
    border-radius: 50%;
    background: var(--tag-white);
  }
  .item-name {
    position: absolute;
    left: 70px;
    top: 232px;
    margin: 0;
    font-size: 82px;
    line-height: 1.13;
    font-weight: 500;
    letter-spacing: 0.5px;
  }
  .translations {
    position: absolute;
    left: 70px;
    top: 520px;
    margin: 0;
    padding: 0;
    list-style: none;
  }
  .translations li {
    font-size: 40px;
    line-height: 66px;
  }
  .lang-zh { font-family: "Noto Sans SC", sans-serif; }
  .lang-ko { font-family: "Noto Sans KR", sans-serif; }
  .lang-ja { font-family: "Noto Sans JP", sans-serif; }
  .lang-es { font-family: "Quicksand", sans-serif; margin-top: 12px; }
  .price {
    position: absolute;
    right: 58px;
    bottom: 62px;
    display: flex;
    align-items: flex-start;
    font-weight: 700;
  }
  .price-currency {
    font-size: 44px;
    line-height: 1;
    margin-top: 12px;
    margin-right: 16px;
    font-weight: 500;
  }
  .price-amount {
    font-size: 176px;
    line-height: 0.8;
    letter-spacing: -2px;
  }
</style>
</head>
<body>
  <main class="price-tag">
    <div class="brand">
      <span class="brand-name">Kumo Kitchen</span>
      <span class="brand-badge"></span>
    </div>

    <h1 class="item-name">Karaage<br>Chicken</h1>

    <ul class="translations">
      <li class="lang-zh" lang="zh">炸鸡</li>
      <li class="lang-ko" lang="ko">가라아게 치킨</li>
      <li class="lang-ja" lang="ja">鶏の唐揚げ</li>
      <li class="lang-es" lang="es">Pollo frito</li>
    </ul>

    <div class="price">
      <span class="price-currency">$</span>
      <span class="price-amount">2.8</span>
    </div>
  </main>
</body>
</html>
```